New Solo Law Office Needs Business Card/Letterhead Design

I am starting a solo law office called "Law Office of Conrad Vashti, PLLC" in Tucson, Arizona. I will be doing criminal defense trial work. More than a logo with any sort of icon, I am really just looking for the name of the company to be displayed in a sleek, minimalist but interesting sort of way, with a format and font type that communicates professionalism. It can be in color, but doesn't have to be, and I am thinking blue and/or red accents colors. I'd like it to convey that I am passionate, dependable and willing to fight. For the business card, I envision sort of higher quality card material, and maybe some embossing or raised print. I will want to include my company name, name, phone and fax numbers, email and website addresses. For the letterhead, I will want to be able to use the same sort of font/formatting design as on the business card.
Industry/Entity Type
Business
Contact Information for Business Card
Law Office of Conrad Vashti, PLLC
Conrad Vashti
conrad@vashti-law.example
www.vashti-law.example
(I do not yet have an established phone or fax number, so please put in some place holder numbers for the formatting, and I can add the actual numbers in before I print.)
Colors
Designer to choose colors to be used in the design.
Look and feel

```html
<!DOCTYPE html>
<html lang="en">
<head>
<meta charset="utf-8">
<title>Conrad Vashti – Business Card</title>
<link rel="stylesheet" href="https://fonts.googleapis.com/css2?family=Baskervville:wght@400;600&display=swap">
<style>
  :root {
    --backdrop: #1d1d1d;
    --paper: #eeeeee;
    --navy: #243451;
    --ink-light: #ffffff;
    --ink-soft: #d9dee7;
  }
  * { margin: 0; padding: 0; box-sizing: border-box; }
  html, body {
    width: 1200px;
    height: 1000px;
    overflow: hidden;
    background: var(--backdrop);
  }
  .card {
    position: absolute;
    left: 250px;
    top: 290px;
    width: 700px;
    height: 420px;
    display: flex;
    font-family: "Baskervville", "Baskerville", Georgia, serif;
  }
  .card-front {
    position: relative;
    width: 319px;
    height: 100%;
    background: var(--paper);
  }
  .firm-name {
    position: absolute;
    left: 0;
    top: 279px;
    width: 352px;
    color: var(--navy);
    font-size: 15px;
    font-weight: 600;
    line-height: 19px;
    text-align: center;
    text-transform: uppercase;
    white-space: nowrap;
  }
  .card-back {
    flex: 1;
    height: 100%;
    background: var(--navy);
    color: var(--ink-light);
    text-align: right;
    padding: 86px 46px 0 0;
  }
  .person-name {
    font-size: 32px;
    font-weight: 600;
    line-height: 36px;
  }
  .person-title {
    margin-top: 2px;
    font-size: 17px;
    color: var(--ink-soft);
    line-height: 22px;
  }
  .address {
    margin-top: 25px;
    font-size: 21px;
    line-height: 26px;
    font-style: normal;
  }
  .contact-list {
    list-style: none;
    margin-top: 7px;
    font-size: 21px;
    line-height: 26.7px;
  }
  .contact-list li {
    display: flex;
    justify-content: flex-end;
    align-items: center;
    gap: 8px;
  }
  .contact-icon {
    width: 14px;
    height: 14px;
    fill: var(--ink-light);
    flex: none;
  }
</style>
</head>
<body>
  <article class="card">
    <section class="card-front">
      <p class="firm-name">Law Office of<br>Conrad Vashti, PLLC</p>
    </section>
    <section class="card-back">
      <h1 class="person-name">Conrad Vashti</h1>
      <p class="person-title">Attorney at Law</p>
      <address class="address">418 Ironwood Avenue<br>Saguaro Vista, Arizona 85700</address>
      <ul class="contact-list">
        <li>
          <svg class="contact-icon" viewBox="0 0 16 16" aria-hidden="true"><path d="M3.2 1.5l2.3-.4 1.3 3-1.5 1.2c.8 1.8 2.2 3.2 4 4l1.2-1.5 3 1.3-.4 2.3c-.2.9-1 1.4-1.9 1.3C6.3 12.3 2.7 8.7 1.9 3.4c-.1-.9.4-1.7 1.3-1.9z"/></svg>
          <span>(520) 555-0148</span>
        </li>
        <li>
          <svg class="contact-icon" viewBox="0 0 16 16" aria-hidden="true"><path d="M4 1h8v4H4zM1.5 6h13c.3 0 .5.2.5.5V12h-3v3H4v-3H1V6.5c0-.3.2-.5.5-.5zM5 10v4h6v-4z"/></svg>
          <span>(520) 555-0172</span>
        </li>
        <li>
          <svg class="contact-icon" viewBox="0 0 16 16" aria-hidden="true"><path d="M1 3h14v10H1zM2.5 4.5v.4L8 9l5.5-4.1v-.4z"/></svg>
          <span>conrad@vashti-law.example</span>
        </li>
        <li>
          <svg class="contact-icon" viewBox="0 0 16 16" aria-hidden="true"><path d="M8 1a7 7 0 100 14A7 7 0 008 1zm5.4 6.3h-2.3c-.1-1.9-.5-3.5-1.2-4.6a5.6 5.6 0 013.5 4.6zM8 2.5c.6.6 1.5 2.3 1.6 4.8H6.4C6.5 4.8 7.4 3.1 8 2.5zM6.1 2.7c-.7 1.1-1.1 2.7-1.2 4.6H2.6a5.6 5.6 0 013.5-4.6zM2.6 8.7h2.3c.1 1.9.5 3.5 1.2 4.6a5.6 5.6 0 01-3.5-4.6zM8 13.5c-.6-.6-1.5-2.3-1.6-4.8h3.2c-.1 2.5-1 4.2-1.6 4.8zm1.9-.2c.7-1.1 1.1-2.7 1.2-4.6h2.3a5.6 5.6 0 01-3.5 4.6z"/></svg>
          <span>www.vashti-law.example</span>
        </li>
      </ul>
    </section>
  </article>
</body>
</html>
```